Kestrel Signs Facebook Banner Design

Design a facebook banner for a sign company. I would like to have a modern approach to it.

Product Offering:
Signs
Banners
Decals
Commercial Wraps

```html
<!DOCTYPE html>
<html lang="en">
<head>
<meta charset="utf-8">
<title>Kestrel Signs – Facebook Cover</title>
<link href="https://fonts.googleapis.com/css2?family=Titillium+Web:ital,wght@0,600;0,700;0,900;1,700;1,900&display=swap" rel="stylesheet">
<style>
  :root {
    --stage: #e9e9ea;
    --cover-bg: #ededee;
    --cover-bg-deep: #dcdcde;
    --line-soft: #d2d2d5;
    --brand-red: #e3262f;
    --brand-red-dark: #b81a22;
    --charcoal: #3b3d42;
    --ink: #2a2b2f;
    --white: #ffffff;
    --van-tone: #3c4a6a;
    --storefront-tone: #8e9096;
    --sign-tone: #b9babd;
  }
  * { box-sizing: border-box; margin: 0; padding: 0; }
  html, body { width: 1200px; height: 714px; overflow: hidden; }
  body {
    background: var(--stage);
    font-family: "Titillium Web", sans-serif;
    position: relative;
  }
  .cover {
    position: absolute;
    left: 0; top: 133px;
    width: 1200px; height: 447px;
    overflow: hidden;
    background: linear-gradient(100deg, var(--cover-bg) 0%, var(--white) 45%, var(--cover-bg-deep) 100%);
  }
  .cover__lines { position: absolute; inset: 0; }
  .brand {
    position: absolute;
    left: 176px; top: 56px;
    color: var(--brand-red);
    font-weight: 900;
    font-size: 50px;
    line-height: 0.86;
    letter-spacing: 1px;
    text-transform: uppercase;
  }
  .brand__line { display: block; }
  .brand__line--second { padding-left: 70px; }
  .contact-band {
    position: absolute;
    left: 0; top: 155px;
    width: 565px; height: 86px;
    background: var(--brand-red);
    clip-path: polygon(0 0, 100% 0, 95% 100%, 0 100%);
  }
  .contact-band__phone {
    position: absolute;
    left: 186px; top: 2px;
    color: var(--white);
    font-style: italic;
    font-weight: 900;
    font-size: 46px;
    line-height: 1.1;
  }
  .contact-band__web {
    position: absolute;
    left: 188px; top: 54px;
    color: var(--white);
    font-style: italic;
    font-weight: 700;
    font-size: 20px;
    letter-spacing: 0.5px;
  }
  .services-band {
    position: absolute;
    left: 0; top: 241px;
    width: 540px; height: 50px;
    background: var(--charcoal);
    clip-path: polygon(0 0, 100% 0, 96% 100%, 0 100%);
    display: flex; align-items: center;
    padding-left: 78px;
    gap: 10px;
    color: var(--white);
    font-weight: 700;
    font-size: 20px;
    letter-spacing: 0.6px;
    text-transform: uppercase;
  }
  .services-band__divider { color: var(--brand-red); }
  .accent { position: absolute; background: var(--brand-red); }
  .accent--tab-a { left: 690px; top: 100px; width: 24px; height: 22px; }
  .accent--tab-b { left: 912px; top: 118px; width: 30px; height: 40px; }
  .accent--tab-c { left: 1120px; top: 137px; width: 26px; height: 28px; }
  .accent--tab-d { left: 686px; top: 356px; width: 60px; height: 8px; }
  .photo-frame {
    position: absolute;
    background: var(--white);
    padding: 7px;
    box-shadow: 0 10px 22px rgba(0,0,0,0.28);
  }
  .photo-frame__fill { width: 100%; height: 100%; }
  .photo-frame--van { left: 543px; top: 76px; width: 183px; height: 216px; transform: rotate(-2deg); }
  .photo-frame--van .photo-frame__fill { background: linear-gradient(160deg, #4c5b7e, var(--van-tone) 55%, #b8252b 100%); }
  .photo-frame--storefront { left: 744px; top: 18px; width: 184px; height: 395px; transform: rotate(2deg); }
  .photo-frame--storefront .photo-frame__fill { background: linear-gradient(180deg, #a7a9ae 0%, var(--storefront-tone) 30%, var(--brand-red-dark) 55%, #6d6f74 100%); }
  .photo-frame--sign { left: 951px; top: 154px; width: 186px; height: 250px; transform: rotate(-3deg); }
  .photo-frame--sign .photo-frame__fill { background: linear-gradient(90deg, #d7d8da 0%, var(--sign-tone) 50%, #cf2a31 100%); }
</style>
</head>
<body>
  <section class="cover" aria-label="Kestrel Signs cover banner">
    <svg class="cover__lines" width="1200" height="447" viewBox="0 0 1200 447" aria-hidden="true">
      <g stroke="var(--line-soft)" stroke-width="2" fill="none">
        <line x1="380" y1="447" x2="860" y2="0"/>
        <line x1="520" y1="447" x2="1000" y2="0"/>
        <line x1="900" y1="447" x2="1200" y2="170"/>
        <line x1="0" y1="120" x2="160" y2="0"/>
      </g>
      <polygon points="560,447 1200,40 1200,80 630,447" fill="var(--cover-bg-deep)" opacity="0.7"/>
    </svg>

    <h1 class="brand">
      <span class="brand__line">Kestrel</span>
      <span class="brand__line brand__line--second">Signs</span>
    </h1>

    <div class="contact-band">
      <p class="contact-band__phone">323-555-0186</p>
      <p class="contact-band__web">WWW.YOURWEBSITE.COM</p>
    </div>

    <ul class="services-band" style="list-style:none">
      <li>Signs</li><li class="services-band__divider">|</li>
      <li>Banners</li><li class="services-band__divider">|</li>
      <li>Decals</li><li class="services-band__divider">|</li>
      <li>Commercial Wraps</li>
    </ul>

    <span class="accent accent--tab-a"></span>
    <span class="accent accent--tab-b"></span>
    <span class="accent accent--tab-c"></span>
    <span class="accent accent--tab-d"></span>

    <figure class="photo-frame photo-frame--van">
      <div class="photo-frame__fill" role="img" aria-label="Photo of a delivery van with a red and black commercial wrap"></div>
    </figure>
    <figure class="photo-frame photo-frame--storefront">
      <div class="photo-frame__fill" role="img" aria-label="Photo of a red outdoor tarpaulin banner hanging on a building front"></div>
    </figure>
    <figure class="photo-frame photo-frame--sign">
      <div class="photo-frame__fill" role="img" aria-label="Photo of a white projecting wall sign mounted on a grey building"></div>
    </figure>
  </section>
</body>
</html>
```